Web presentation for K.teravinu & Partners A Professional Law Corporation

To design a full detailed web presentation for the above mentioned corporation.

It Professional

```html
<!DOCTYPE html>
<html lang="en">
<head>
<meta charset="utf-8">
<title>K.teravinu &amp; Partners — A Professional Law Corporation</title>
<link rel="stylesheet" href="https://fonts.googleapis.com/css2?family=Oswald:wght@400;500;600&family=Open+Sans:wght@400;600&display=swap">
<style>
:root{
  --navy:#0e0b7c;
  --indigo:#2c2596;
  --lavender:#c7c3ef;
  --title-lilac:#c9c5f2;
  --ink:#222;
  --muted:#8a8a8a;
  --dark:#383c44;
  --darker:#2e3238;
  --white:#fff;
  --line:#d8d8d8;
}
*{box-sizing:border-box;margin:0;padding:0}
html,body{width:1200px;height:2910px;overflow:hidden}
body{position:relative;background:var(--white);font-family:"Open Sans",Arial,sans-serif;color:var(--ink)}
.abs{position:absolute}
.heading{font-family:"Oswald",Arial,sans-serif}
.center{text-align:center;left:0;width:1200px}

/* hero */
.hero{top:0;left:0;width:1200px;height:480px;background:radial-gradient(ellipse at 55% 55%,#7a7a7a 0%,#4a4a4a 45%,#262626 100%)}
.brand{top:28px;left:260px;color:#e8e8e8;font-family:"Oswald",Arial,sans-serif;font-weight:500;letter-spacing:.5px}
.brand-name{font-size:25px;line-height:32px}
.brand-tag{font-size:16px;line-height:22px;letter-spacing:1.2px}
.nav{top:42px;left:656px;display:flex;gap:34px;font-family:"Oswald",Arial,sans-serif;font-size:12px;color:var(--white)}
.hero-title{top:176px;font-family:"Oswald",Arial,sans-serif;font-weight:600;font-size:44px;color:var(--title-lilac)}
.hero-sub{top:242px;font-size:15px;color:#eee}
.btn{display:flex;align-items:center;justify-content:center;font-family:"Oswald",Arial,sans-serif;font-size:11px;border-radius:4px}
.btn-navy{background:var(--navy);color:var(--white)}
.hero-btn{top:280px;left:535px;width:126px;height:30px}
.scroll-down{top:426px;left:587px}

/* services */
.service{top:542px;width:220px;text-align:center}
.service-ring{width:92px;height:92px;margin:0 auto;border:1px solid var(--line);border-radius:50%;display:flex;align-items:center;justify-content:center}
.service-name{margin-top:18px;font-family:"Oswald",Arial,sans-serif;font-size:11px;color:#444}
.service-text{margin-top:18px;font-size:8.5px;line-height:10.5px;color:#333}

/* newsletter */
.newsletter{top:778px;left:0;width:1200px;height:148px;background:linear-gradient(90deg,#2c3036,#4c5058 50%,#2c3036)}
.field{background:var(--white);border-radius:5px;font-size:9px;color:#666;padding:0 12px;display:flex;align-items:center}
.news-input{top:836px;left:340px;width:336px;height:30px}
.news-btn{top:836px;left:694px;width:162px;height:30px}

/* news */
.section-title{font-family:"Oswald",Arial,sans-serif;font-size:21px;color:#222}
.section-title span{color:var(--indigo)}
.news-title{top:978px}
.news-sub{top:1015px;left:458px;width:284px;text-align:center;font-size:9px;line-height:17px;color:#444}
.tile{width:216px;height:216px;border-radius:5px}
.tile-feature{background:var(--navy);color:var(--white);text-align:center;padding-top:44px}
.tile-feature h3{font-family:"Oswald",Arial,sans-serif;font-weight:400;font-size:16px}
.tile-feature p{margin:12px auto 0;width:176px;font-size:9px;line-height:13px}
.read-more{margin:22px auto 0;width:126px;height:28px;background:var(--white);color:var(--navy)}
.show-more{top:1614px;left:536px;width:126px;height:30px;border:1px solid var(--line);color:#333}

/* testimonial */
.testimonial{top:1702px;left:0;width:1200px;height:300px;background:linear-gradient(90deg,#27228a,#3b35a8 50%,#2a2490)}
.avatar{border-radius:50%;background:radial-gradient(circle at 50% 40%,#d9d4cf,#8c8a90)}
.quote{top:1860px;font-size:15px;line-height:24px;color:var(--white)}
.quote-name{top:1926px;font-size:12px;color:#e6e6f5}

/* team */
.team-title{top:2056px}
.member{top:2164px;width:160px;text-align:center}
.member .avatar{width:80px;height:80px;margin:0 auto;border:2px solid #eee}
.member-name{margin-top:18px;font-size:10px;color:#333}
.member-role{font-size:10px;color:var(--muted)}

/* contact */
.contact{top:2358px;left:0;width:1200px;height:480px;background:linear-gradient(180deg,#2f333a,#3c4048)}
.say-hello{top:2408px;font-family:"Oswald",Arial,sans-serif;font-size:22px;color:var(--white)}
.address{top:2450px;font-size:9px;line-height:19px;color:#e6e6e6}
.contact-email{top:2538px;left:350px;width:240px;height:30px}
.contact-subject{top:2538px;left:606px;width:242px;height:30px}
.contact-message{top:2590px;left:350px;width:498px;height:118px;align-items:flex-start;padding-top:8px}
.contact-btn{top:2724px;left:350px;width:126px;height:30px;background:var(--lavender);color:var(--navy)}
.social{top:2726px;left:746px;display:flex;gap:9px}
.social span{width:24px;height:24px;border-radius:50%;background:#cfd0d6}

.footer{top:2838px;left:0;width:1200px;height:72px;background:var(--darker);color:#e0e0e0;font-size:9px;display:flex;align-items:center;justify-content:center}
</style>
</head>
<body>

<header>
  <div class="abs hero" role="img" aria-label="Black and white photograph of a statue of justice, an open book and a gavel on a desk"></div>
  <div class="abs brand">
    <div class="brand-name">K.TERAVINU &amp; PARTNERS</div>
    <div class="brand-tag">A Professional Law Corporation</div>
  </div>
  <nav class="abs nav"><span>ABOUT US</span><span>SERVICES</span><span>NEWS &amp; EVENTS</span><span>OUR TEAM</span></nav>
  <h1 class="abs center hero-title">CONSCIENTIOUS</h1>
  <p class="abs center hero-sub">We exercise the utmost care in assisting our clients.</p>
  <div class="abs btn btn-navy hero-btn">HIRE US</div>
  <svg class="abs scroll-down" width="24" height="24" viewBox="0 0 24 24"><circle cx="12" cy="12" r="10.5" fill="none" stroke="#fff" stroke-width="1.2"/><path d="M7.5 10.5l4.5 4 4.5-4" fill="none" stroke="#fff" stroke-width="1.4"/></svg>
</header>

<section class="services">
  <div class="abs service" style="left:254px">
    <div class="service-ring"><svg width="34" height="34" viewBox="0 0 34 34" fill="none" stroke="#2c2596" stroke-width="1.4"><rect x="7" y="4" width="20" height="26" rx="1.5"/><path d="M11 11h12M11 15h12M11 19h7"/><circle cx="22" cy="24" r="3"/></svg></div>
    <div class="service-name">SERVICE 1</div>
    <p class="service-text">We draft and review contracts with care, protect your interests in every clause and guide you through each step of the agreement.</p>
  </div>
  <div class="abs service" style="left:488px">
    <div class="service-ring"><svg width="34" height="34" viewBox="0 0 34 34" fill="none" stroke="#2c2596" stroke-width="1.4"><rect x="6" y="14" width="22" height="14" rx="1.5"/><path d="M13 14v14M21 14v14M6 20h22"/><circle cx="10" cy="9" r="3"/><circle cx="17" cy="8" r="3"/><circle cx="24" cy="9" r="3"/></svg></div>
    <div class="service-name">SERVICE 2</div>
    <p class="service-text">Our litigation team prepares every case in depth, represents you in court and works toward a fair and timely result for your matter.</p>
  </div>
  <div class="abs service" style="left:726px">
    <div class="service-ring"><svg width="34" height="34" viewBox="0 0 34 34" fill="none" stroke="#2c2596" stroke-width="1.4"><path d="M7 18a10 10 0 0 1 20 0z"/><path d="M5 18h24M17 8v4"/><path d="M9 30c1-5 4-8 8-8s7 3 8 8"/></svg></div>
    <div class="service-name">SERVICE 3</div>
    <p class="service-text">We advise builders and contractors on permits, claims and project risk so that work on site can move ahead with fewer delays.</p>
  </div>
</section>

<section>
  <div class="abs newsletter" role="img" aria-label="Dark blurred photograph of legal papers on a desk"></div>
  <div class="abs field news-input">Enter Your email adress for newsletter</div>
  <div class="abs btn btn-navy news-btn">SUBSCRIBE</div>
</section>

<section>
  <h2 class="abs center section-title news-title">OUR <span>NEWS &amp; EVENTS</span></h2>
  <p class="abs news-sub">Updates on recent cases, public tenders, seminars and firm events, shared with our clients and partners.</p>
  <div class="abs tile" style="left:260px;top:1106px;background:linear-gradient(160deg,#8d8f96,#4b4d55 60%,#d8d8d8)" role="img" aria-label="Photograph of colleagues reviewing work at a computer"></div>
  <div class="abs tile" style="left:492px;top:1106px;background:linear-gradient(180deg,#7aa4d8,#b9cfe6 50%,#d27a3a)" role="img" aria-label="Photograph of a construction worker in a hard hat near a crane"></div>
  <div class="abs tile" style="left:724px;top:1106px;background:linear-gradient(160deg,#b07e5a,#5a4032 55%,#2a2320)" role="img" aria-label="Photograph of a speaker at a press event with a microphone"></div>
  <div class="abs tile" style="left:260px;top:1338px;background:linear-gradient(180deg,#e8e4df,#b8aea4 60%,#6c5a4c)" role="img" aria-label="Photograph of a presenter addressing a seated audience"></div>
  <div class="abs tile" style="left:492px;top:1338px;background:linear-gradient(150deg,#f0f0ef,#c8c9cc 60%,#8d8f94)" role="img" aria-label="Photograph of documents and a tablet on a white desk"></div>
  <div class="abs tile tile-feature" style="left:724px;top:1338px">
    <h3>BID PROTESTS</h3>
    <p>Challenging contract awards with a clear and timely protest strategy.</p>
    <div class="btn read-more">READ MORE</div>
  </div>
  <div class="abs btn show-more">SHOW MORE</div>
</section>

<section>
  <div class="abs testimonial" role="img" aria-label="Blue tinted photograph of an office with plants"></div>
  <div class="abs avatar" style="left:562px;top:1764px;width:72px;height:72px;border:2px solid #fff" role="img" aria-label="Portrait of the client"></div>
  <svg class="abs" style="left:200px;top:1838px" width="16" height="28" viewBox="0 0 16 28"><path d="M13 2L3 14l10 12" fill="none" stroke="#8c88d6" stroke-width="1.6"/></svg>
  <svg class="abs" style="left:980px;top:1838px" width="16" height="28" viewBox="0 0 16 28"><path d="M3 2l10 12L3 26" fill="none" stroke="#8c88d6" stroke-width="1.6"/></svg>
  <p class="abs center quote">These guys are incredible! I get my case in 10 days and it was awesome!<br>Very good service! Highly recommended!</p>
  <p class="abs center quote-name">Daniel Reyes</p>
</section>

<section>
  <h2 class="abs center section-title team-title">OUR <span>TEAM</span></h2>
  <div class="abs member" style="left:234px"><div class="avatar" role="img" aria-label="Portrait of a team member"></div><div class="member-name">MEMBER NAME</div><div class="member-role">Designation</div></div>
  <div class="abs member" style="left:424px"><div class="avatar" role="img" aria-label="Portrait of a team member"></div><div class="member-name">MEMBER NAME</div><div class="member-role">Designation</div></div>
  <div class="abs member" style="left:614px"><div class="avatar" role="img" aria-label="Portrait of a team member"></div><div class="member-name">MEMBER NAME</div><div class="member-role">Designation</div></div>
  <div class="abs member" style="left:808px"><div class="avatar" role="img" aria-label="Portrait of a team member"></div><div class="member-name">MEMBER NAME</div><div class="member-role">Designation</div></div>
</section>

<footer>
  <div class="abs contact"></div>
  <h2 class="abs center say-hello">SAY HELLO: +1 555 014 2290</h2>
  <p class="abs center address">address ln1<br>Twelve Harbor Row, Suite 210<br>location 1 location 2</p>
  <div class="abs field contact-email">Your Email</div>
  <div class="abs field contact-subject">Subject</div>
  <div class="abs field contact-message">Your Message</div>
  <div class="abs btn contact-btn">HIRE US</div>
  <div class="abs social"><span></span><span></span><span></span></div>
  <div class="abs footer">© 2017 Copyright K.teravinu &amp; Partners</div>
</footer>

</body>
</html>
```